Healing stone/crystal Shopify store

Hi - I'm creating a new site to sell healing crystals/stones.Name for the shop is LumaraBloomHouse. Site helps people to choose best crystals for them .Shop should have blog aswell.The site should be informative and attractive. Stones we sell Opalite,Green Aventurine,Watermelon Crystal,Rose Quartz Stone,Tiger Eye Stone. Must be Shopify. No content yet, you can fill neccessary fields Lorea Ipsum and if you have some good idea you can put it there
Updates

Designs look the same

Target Market(s)

Woman, English speaking countries.

Industry/Entity Type

Shop

Number of Pages Required

1 page

Colors

Designer to choose colors to be used in the design.

Requirements
Must have
• Blog
Nice to have
• High quality pictures to look site attractive.

```html
<!DOCTYPE html>
<html lang="en">
<head>
<meta charset="utf-8">
<title>Lumara Bloom House</title>
<link rel="stylesheet" href="https://fonts.googleapis.com/css2?family=Mulish:wght@300;400;600;700;800&display=swap">
<style>
:root{
  --teal:#2fbe9c;
  --dark:#1b1b1b;
  --ink:#222;
  --muted:#555;
  --paper:#fbfbfa;
  --white:#fff;
  --line:#e6e6e6;
}
*{box-sizing:border-box;margin:0;padding:0}
html,body{width:1200px;height:2560px;overflow:hidden}
body{position:relative;background:var(--paper);font-family:"Mulish",sans-serif;color:var(--ink)}
.abs{position:absolute}
.topbar{left:0;top:0;width:1200px;height:40px;background:var(--dark)}
.nav{left:160px;top:0;display:flex;height:40px}
.nav a{color:var(--white);font-size:11px;font-weight:700;text-decoration:none;display:flex;align-items:center;padding:0 20px;letter-spacing:.3px}
.nav a.active{background:var(--teal)}
.social{left:872px;top:14px;display:flex;gap:10px}
.social span{width:11px;height:11px;border-radius:50%;background:#ddd;display:block}
.header-contact{top:80px;font-size:17px;font-weight:700;display:flex;align-items:center;gap:10px;white-space:nowrap}
.brand{left:0;width:1200px;top:66px;text-align:center;font-size:40px;font-weight:300;letter-spacing:.3px;white-space:nowrap}
.media{display:block}
.section-title{left:0;width:1200px;text-align:center;font-weight:400;font-size:38px;letter-spacing:.5px}
.section-sub{left:0;width:1200px;text-align:center;font-size:9px;color:#888}
.card{width:270px}
.card h3{font-size:16px;font-weight:700;margin-top:32px}
.card p{font-size:11px;line-height:17px;color:var(--muted);margin-top:12px}
.card .more{display:block;font-size:11px;font-weight:800;margin-top:16px}
.arrow{width:52px;height:52px;border-radius:50%;background:#ececec;display:flex;align-items:center;justify-content:center}
.about-text{left:599px;top:1111px;width:473px;height:371px;background:var(--teal);color:var(--white);padding:30px 38px}
.about-text h2{font-weight:400;font-size:36px;line-height:44px}
.about-text p{font-size:12px;line-height:18px;margin-top:26px}
.about-text p + p{margin-top:18px}
.blog-intro{left:200px;width:800px;top:1608px;text-align:center;font-size:12px;line-height:18px;color:var(--muted)}
.date{left:559px;top:1763px;width:76px;height:76px;border-radius:50%;background:#5a3b3e;color:var(--white);text-align:center;padding-top:12px}
.date b{display:block;font-size:26px;font-weight:400;line-height:28px}
.date small{font-size:11px}
.caption{top:1955px;font-size:15px;font-weight:600}
.footer{left:0;top:2009px;width:1200px;height:500px;background:var(--teal);color:var(--white)}
.field{position:absolute;border-bottom:2px solid var(--white);text-align:center;font-size:14px;padding-bottom:12px}
.submit{position:absolute;left:498px;top:217px;width:200px;height:44px;border:2px solid var(--white);display:flex;align-items:center;justify-content:center;font-size:13px;font-weight:700}
.divider{position:absolute;left:160px;top:326px;width:880px;height:1px;background:rgba(255,255,255,.3)}
.links{position:absolute;top:380px;list-style:none;font-size:12px;line-height:19px}
.links li::before{content:"- "}
.address{position:absolute;left:582px;top:374px;font-size:12px;line-height:16px}
.big-phone{position:absolute;left:850px;top:396px;font-size:22px;display:flex;align-items:center;gap:10px}
.copyright{left:0;width:1200px;top:2527px;text-align:center;font-size:11px;color:#777}
</style>
</head>
<body>
<div class="abs topbar"></div>
<nav class="abs nav">
  <a class="active">HOME</a><a>ABOUT US</a><a>PRODUCTS</a><a>BLOGS</a><a>CONTACT US</a>
</nav>
<div class="abs social" aria-hidden="true"><span></span><span></span><span></span><span></span><span></span><span></span><span></span>
  <svg width="13" height="13" viewBox="0 0 13 13"><circle cx="5.5" cy="5.5" r="4" fill="none" stroke="#ddd" stroke-width="1.5"/><path d="M8.5 8.5l3.5 3.5" stroke="#ddd" stroke-width="1.5"/></svg>
</div>

<div class="abs header-contact" style="left:160px">
  <svg width="14" height="22" viewBox="0 0 14 22"><rect x="1" y="1" width="12" height="20" rx="2" fill="none" stroke="#222" stroke-width="2"/><rect x="5" y="17" width="4" height="1.5" fill="#222"/></svg>
  001-555-0142</div>
<div class="abs brand">Lumara Bloom House</div>
<div class="abs header-contact" style="left:840px;font-weight:400;font-size:15px">
  <svg width="20" height="14" viewBox="0 0 20 14"><rect x="1" y="1" width="18" height="12" fill="none" stroke="#222" stroke-width="1.8"/><path d="M1 1l9 7 9-7" fill="none" stroke="#222" stroke-width="1.8"/></svg>
  info@lumarabloomhouse.com</div>

<div class="abs media" role="img" aria-label="Carved crystal angels and an elephant above matching tumbled stones on pale stone" style="left:128px;top:142px;width:944px;height:423px;background:linear-gradient(90deg,#d9d5de,#e7e3de 30%,#e9eae6 55%,#dfe7e0 75%,#ead7d6)"></div>

<h2 class="abs section-title" style="top:625px">OUR PRODUCTS</h2>
<div class="abs section-sub" style="top:674px">LUMARA BLOOM HOUSE</div>

<div class="abs arrow" style="left:78px;top:844px"><svg width="12" height="18" viewBox="0 0 12 18"><path d="M9 2L3 9l6 7" fill="none" stroke="#888" stroke-width="2"/></svg></div>
<div class="abs arrow" style="left:1070px;top:844px"><svg width="12" height="18" viewBox="0 0 12 18"><path d="M3 2l6 7-6 7" fill="none" stroke="#888" stroke-width="2"/></svg></div>

<div class="abs card" style="left:160px;top:710px">
  <div class="media" role="img" aria-label="Stacked dark stones with a white flower over calm water" style="height:190px;background:linear-gradient(180deg,#bfe3e6,#7fc9cf 60%,#4a8e99)"></div>
  <h3>Crystals / Stone</h3>
  <p>Lorem ipsum dolor sit amet, consectetur adipiscing elit, Lorem ipsum dolor sit amet, consectetur adipiscing elit,</p>
  <span class="more">MORE &#8594;</span>
</div>
<div class="abs card" style="left:464px;top:710px">
  <div class="media" role="img" aria-label="Row of smooth grey stones fading into still water" style="height:190px;background:linear-gradient(180deg,#f3f2ee,#d8d9d8 55%,#9da3a7)"></div>
  <h3>Crystals / Stone</h3>
  <p>Lorem ipsum dolor sit amet, consectetur adipiscing elit, Lorem ipsum dolor sit amet, consectetur adipiscing elit,</p>
  <span class="more">MORE &#8594;</span>
</div>
<div class="abs card" style="left:770px;top:710px">
  <div class="media" role="img" aria-label="Ring of carved crystal angels on a dark surface" style="height:190px;background:linear-gradient(160deg,#5a5961,#4a4950 55%,#3f3e45)"></div>
  <h3>Crystals / Stone</h3>
  <p>Lorem ipsum dolor sit amet, consectetur adipiscing elit, Lorem ipsum dolor sit amet, consectetur adipiscing elit,</p>
  <span class="more">MORE &#8594;</span>
</div>

<div class="abs media" role="img" aria-label="Circle of opalite, rose quartz, aventurine and tiger eye angels on dark grey" style="left:128px;top:1111px;width:471px;height:371px;background:linear-gradient(160deg,#5b5a62,#4a4950 55%,#3d3c43)"></div>
<div class="abs about-text">
  <h2>ABOUT LUMARA STONE STUDIO</h2>
  <p>Lorem ipsum dolor sit amet, consectetur adipiscing elit,Lorem ipsum dolor sit amet, consectetur adipiscing elit, sed do eiusmod tempor incididunt ut labore et dolore magna aliqua.Ut enim ad minim veniam, quis nostrud exercitation ullamco laboris nisi ut aliquip ex ea commodo consequat.Lorem ipsum dolor sit amet, consectetur adipiscing elit,Lorem ipsum dolor sit amet,</p>
  <p>sed do eiusmod tempor incididunt ut labore et dolore magna aliqua.Ut enim ad minim veniam, quis nostrud exercitation ullamco laboris nisi ut aliquip ex ea commodo consequat.</p>
</div>

<h2 class="abs section-title" style="top:1545px">LATEST BLOGS</h2>
<p class="abs blog-intro">sed do eiusmod tempor incididunt ut labore et dolore magna aliqua.Ut enim ad minim veniam, quis nostrud exercitation ullamco laboris nisi ut aliquip ex ea commodo consequat.</p>

<div class="abs media" role="img" aria-label="Pile of pastel crystal chips" style="left:170px;top:1683px;width:190px;height:255px;background:linear-gradient(90deg,rgba(251,251,250,1),rgba(232,215,205,.85) 60%,#dcc8bd)"></div>
<div class="abs media" role="img" aria-label="Pink heart stone among grey river pebbles" style="left:376px;top:1683px;width:447px;height:255px;background:linear-gradient(135deg,#b3a697,#9c968d 50%,#8a8680)"></div>
<div class="abs media" role="img" aria-label="Heap of colourful polished agate stones" style="left:840px;top:1683px;width:153px;height:255px;background:linear-gradient(90deg,#9a6a78,#a4a0b8 55%,rgba(251,251,250,1))"></div>
<div class="abs date"><b>5</b><small>MAR</small></div>
<div class="abs arrow" style="left:150px;top:1784px;background:rgba(230,230,230,.9)"><svg width="12" height="18" viewBox="0 0 12 18"><path d="M9 2L3 9l6 7" fill="none" stroke="#888" stroke-width="2"/></svg></div>
<div class="abs arrow" style="left:996px;top:1784px;background:rgba(230,230,230,.9)"><svg width="12" height="18" viewBox="0 0 12 18"><path d="M3 2l6 7-6 7" fill="none" stroke="#888" stroke-width="2"/></svg></div>
<div class="abs caption" style="left:376px">Lorem Ipsum Dolor Sit...</div>
<div class="abs caption" style="left:772px;font-size:12px;font-weight:800">More &#10230;</div>

<footer class="abs footer">
  <div class="field" style="left:178px;top:66px;width:264px">Full Name</div>
  <div class="field" style="left:466px;top:66px;width:266px">Email</div>
  <div class="field" style="left:758px;top:66px;width:264px">Phone</div>
  <div class="field" style="left:182px;top:137px;width:840px">Message</div>
  <div class="submit">SUBMIT</div>
  <div class="divider"></div>
  <ul class="links" style="left:160px"><li>Home</li><li>About Us</li><li>Products</li><li>Blogs</li></ul>
  <ul class="links" style="left:338px"><li>Terms &amp; Condition</li><li>Privacy Policy</li><li>Contact Us</li></ul>
  <div class="address">
    <div style="display:flex;gap:10px">
      <svg width="14" height="20" viewBox="0 0 14 20"><path d="M7 1a6 6 0 0 0-6 6c0 5 6 12 6 12s6-7 6-12a6 6 0 0 0-6-6z" fill="#fff"/><circle cx="7" cy="7" r="2.2" fill="#2fbe9c"/></svg>
      <span>Excepteur sint occaecat Lorem<br>cupidatat non proident<br>Dolor Sit Amet</span>
    </div>
    <div style="display:flex;gap:10px;margin-top:14px;align-items:center">
      <svg width="14" height="10" viewBox="0 0 14 10"><rect width="14" height="10" fill="#fff"/><path d="M0 0l7 5 7-5" fill="none" stroke="#2fbe9c"/></svg>
      <span>info@lumarabloomhouse.com</span>
    </div>
  </div>
  <div class="big-phone">
    <svg width="18" height="18" viewBox="0 0 18 18"><path d="M4 1l3 4-2 2c1 2 3 4 5 5l2-2 4 3-2 3C8 16 2 10 1 4z" fill="#fff"/></svg>
    0012 - 555 - 019</div>
</footer>
<div class="abs copyright">Copyrights&copy; 2018 Lumara Bloom House Allrights are Reserved.</div>
</body>
</html>
```